Business Card Trevian Digital

Design of two business cards (board) for Trevian Digital. Trevian Digital DMCC, based in in Dubai U.A.E. Trevian Digital is a self-contained online company, taking an online concept from idea to reality. Concretely, this has involved the (partly remote) management, website development, market implementation and mobile application development for several platforms.

Frontside of business card should feature our company logo (Trevian) and personal details. Backside should feature the logo's of our current brands (mendquickly, taskpalace and galaplanner). We would prefer a design based on the grey/orange color scheme of our company. Trevian Digital is a young, modern and dynamic company and we would like to see this reflected in the design.

```html
<!DOCTYPE html>
<html lang="en">
<head>
<meta charset="utf-8">
<title>Trevian Digital – Business Card</title>
<link rel="stylesheet" href="https://fonts.googleapis.com/css2?family=Lato:wght@400;700&display=swap">
<style>
  :root {
    --board: #e4e4e4;
    --card: #ffffff;
    --orange: #f0522a;
    --grey: #3a3a3c;
    --mark-grey: #58585a;
    --brand-orange: #f4922e;
    --brand-teal: #5bc4c6;
    --brand-green: #a6cf4a;
  }
  * { margin: 0; padding: 0; box-sizing: border-box; }
  html, body {
    width: 992px;
    height: 1200px;
    overflow: hidden;
    background: var(--board);
    font-family: "Lato", Arial, sans-serif;
  }
  .board { position: relative; width: 992px; height: 1200px; }
  .card {
    position: absolute;
    background: var(--card);
  }
  .card--front { left: 79px; top: 61px; width: 839px; height: 477px; }
  .card--back  { left: 77px; top: 637px; width: 841px; height: 479px; }

  /* Front: brand block */
  .brand-block {
    position: absolute;
    left: 93px; top: 134px;
    width: 210px;
    display: flex;
    flex-direction: column;
    align-items: center;
  }
  .brand-dot {
    width: 130px; height: 130px;
    border-radius: 50%;
    background: var(--mark-grey);
    margin-bottom: 52px;
  }
  .brand-name {
    color: var(--orange);
    font-size: 34px;
    font-weight: 400;
    letter-spacing: 6px;
    line-height: 1;
  }

  /* Front: details */
  .details {
    position: absolute;
    left: 360px; top: 66px;
    width: 400px;
    text-align: center;
  }
  .company-name {
    color: var(--orange);
    font-size: 30.5px;
    font-weight: 700;
    letter-spacing: 0.2px;
  }
  .person-name {
    margin-top: 40px;
    font-size: 41px;
    font-weight: 400;
    line-height: 1;
    color: var(--orange);
  }
  .person-name .surname { color: var(--grey); font-weight: 700; }
  .person-role {
    margin-top: 4px;
    color: var(--orange);
    font-size: 22px;
  }
  .contact-list {
    list-style: none;
    margin-top: 55px;
    color: var(--orange);
    font-size: 17px;
    line-height: 35.5px;
  }

  /* Back: brands */
  .brand-lockup {
    display: flex;
    align-items: center;
  }
  .brand-lockup__square { flex: none; }
  .brand-lockup__name {
    color: var(--mark-grey);
    font-weight: 700;
    line-height: 1;
  }
  .brand-lockup--main {
    position: absolute;
    left: 0; right: 0; top: 237px;
    justify-content: center;
    gap: 26px;
  }
  .brand-lockup--main .brand-lockup__square {
    width: 62px; height: 62px;
    background: var(--brand-orange);
  }
  .brand-lockup--main .brand-lockup__name {
    font-size: 60px;
    letter-spacing: 1px;
  }
  .brand-row {
    position: absolute;
    left: 0; right: 0; top: 352px;
    display: flex;
    justify-content: center;
    gap: 70px;
  }
  .brand-row .brand-lockup { gap: 14px; }
  .brand-row .brand-lockup__square { width: 30px; height: 30px; }
  .brand-row .brand-lockup__name { font-size: 32px; }
  .square--teal { background: var(--brand-teal); }
  .square--green { background: var(--brand-green); }
</style>
</head>
<body>
<main class="board">
  <section class="card card--front">
    <div class="brand-block">
      <div class="brand-dot"></div>
      <div class="brand-name">TREVIAN</div>
    </div>
    <div class="details">
      <h1 class="company-name">YOUR COMPANY NAME</h1>
      <p class="person-name">YOUR <span class="surname">NAME</span></p>
      <p class="person-role">Director</p>
      <ul class="contact-list">
        <li>+ 000 - 1234 - 5678</li>
        <li>admin@your e-mail.com</li>
        <li>your web site.com</li>
        <li>000 Seventh Avenue, New York 12345</li>
      </ul>
    </div>
  </section>

  <section class="card card--back">
    <div class="brand-lockup brand-lockup--main">
      <div class="brand-lockup__square"></div>
      <span class="brand-lockup__name">mendquickly</span>
    </div>
    <div class="brand-row">
      <div class="brand-lockup">
        <div class="brand-lockup__square square--teal"></div>
        <span class="brand-lockup__name">taskpalace</span>
      </div>
      <div class="brand-lockup">
        <div class="brand-lockup__square square--green"></div>
        <span class="brand-lockup__name">galaplanner</span>
      </div>
    </div>
  </section>
</main>
</body>
</html>
```